Website re-design wedding music business

I need my wordpress wedding music website redesigned. I'm a wedding pianist and also provide duo/trio entertainment with other musicians and looking for an overhaul of my wordpress site.

Website: tollykessing.com.au

Target Market(s)

brides; engaged couples

Industry/Entity Type

Wedding

Number of Pages Required

5+ page

Colors

Designer to choose colors to be used in the design.

Requirements
Must have
• I'm looking to overhaul my website which is looking rather tired after 4 years. It is functional but not inviting to visitors. Initially my website started out as a solo piano player providing music for wedding. It is gradually growing now where brides can book
• 1) Solo Piano
• 2) Duo (any combination of Piano / Cello / Vocalist / Violin)
• 3) Trio (any combination of Piano/ Cello /Vocalist / Violin)
• in future it may increase to 4 / 5 /6 piece bands so that needs to be taken into account for the future growth where I'll recruit other musicians.
• Some other functionality I'd like to see
• - Visitors want a calendar to know availability of musicians
• - Automatically providing enquiry price & discount (if applicable)
• - Automating the booking form process (manual) - There's a PDF form I send to the customer after we go back/forth on email on songs/price etc but if more of it could be automated online that would be great. If move to online it would be good to be able to override the set prices with a custom price and also providing a payment gateway
• More Flexibility on pricing - customer selects type of artists they want and it calculates a price based on who they have chosen whether it is a ceremony or canapes or reception (or combination of any). Extra transport fee is added if >50km out of Melbourne.
• How would you re-design this website. Imagine you are a bride/groom looking to book wedding music services. I would love to see some concepts .
• Please indicate any other fees required for your submission and level of support post this competition. I would like this to be an on-going relationship.
Nice to have
• I'd preferably like the website to be in wordpress as I've been familiar with it over time and can do basic updates in the back end. Happy for other suggestions if you can convince me I should move away from wordpress.

```html
<!DOCTYPE html>
<html lang="en">
<head>
<meta charset="utf-8">
<title>Tolly Kessing | Wedding Pianist</title>
<link href="https://fonts.googleapis.com/css2?family=Titillium+Web:wght@300;400;600;700&family=Open+Sans:wght@400;600&display=swap" rel="stylesheet">
<style>
:root{
  --pink:#e8265a;
  --pink-dark:#b9174a;
  --pink-deep:#8f1238;
  --ink:#1e1e23;
  --ink-soft:#2b2b31;
  --grey:#f1f1f3;
  --line:#dedee2;
  --text:#555;
  --white:#fff;
}
*{box-sizing:border-box;margin:0;padding:0}
html,body{width:1200px;height:3116px;overflow:hidden}
body{font-family:"Open Sans",sans-serif;color:var(--text);background:var(--white);font-size:13px}
h1,h2,h3,.nav,.btn{font-family:"Titillium Web",sans-serif}

.topbar{height:40px;background:var(--ink);display:flex;align-items:center;justify-content:space-between;padding:0 40px}
.socials{display:flex;gap:8px}
.socials span{width:18px;height:18px;border-radius:50%;background:#55555c;display:block}
.toplinks{display:flex;gap:22px;font-size:10px;color:#bbb;letter-spacing:.5px;text-transform:uppercase}

.header{height:48px;display:flex;align-items:center;justify-content:space-between;padding:0 40px;border-bottom:1px solid var(--line)}
.brand{display:flex;align-items:center;gap:8px;font-family:"Titillium Web",sans-serif;font-weight:700;font-size:17px;color:var(--ink);letter-spacing:1px}
.brand i{width:22px;height:22px;border-radius:50%;background:var(--ink);display:block}
.nav{display:flex;align-items:center;gap:26px;font-size:12px;font-weight:600;color:#666;letter-spacing:.5px}
.nav .active{color:var(--pink);border-bottom:2px solid var(--pink);padding-bottom:3px}
.btn{background:var(--pink);color:var(--white);font-weight:700;border-radius:3px;display:inline-flex;align-items:center;justify-content:center;letter-spacing:1px;text-transform:uppercase}
.nav .btn{padding:7px 16px;border-radius:16px;font-size:11px}

.hero{height:552px;position:relative;background:linear-gradient(180deg,#e9e9ec,#f7f7f8 70%,#e6e6e9)}
.hero-photo{position:absolute;left:120px;top:0;width:520px;height:552px;background:linear-gradient(160deg,#d6d6da,#9a9aa2 55%,#e2e2e5)}
.hero-text{position:absolute;left:716px;top:150px;width:380px}
.hero-text h1{font-size:44px;font-weight:300;color:var(--ink);letter-spacing:2px;line-height:1}
.hero-text h1 b{font-weight:700}
.hero-text .role{color:var(--pink);font-family:"Titillium Web",sans-serif;font-weight:700;font-size:17px;letter-spacing:1px;margin:8px 0 14px}
.hero-text p{font-size:13px;line-height:1.6;color:#666}
.hero-text .btn{margin-top:22px;padding:10px 24px;font-size:12px;border-radius:18px}
.badges{display:flex;gap:24px;margin-top:34px}
.badges span{width:60px;height:60px;border-radius:50%;background:#2e2e33;border:4px solid #c9a94c}

.section-title{text-align:center}
.section-title h2{font-size:30px;font-weight:700;letter-spacing:1.5px;text-transform:uppercase}
.section-title svg{display:block;margin:6px auto 0}

.music{height:660px;position:relative;background:linear-gradient(135deg,#f0376a,var(--pink) 40%,var(--pink-dark));padding-top:52px}
.music .section-title h2{color:var(--white)}
.music-panel{position:absolute;left:140px;top:112px;width:920px;height:488px;background:rgba(60,10,28,.78);display:flex;gap:24px;padding:20px}
.panel-col{flex:1}
.panel-col h3{color:var(--white);font-size:17px;font-weight:700;text-transform:uppercase;letter-spacing:1px;border-bottom:1px solid rgba(255,255,255,.2);padding-bottom:8px;margin-bottom:14px}
.player{background:var(--white);height:90px;border-radius:2px;display:flex;align-items:center;gap:16px;padding:0 18px}
.play{width:50px;height:50px;border-radius:50%;border:2px solid var(--pink);display:flex;align-items:center;justify-content:center}
.player .track{flex:1;font-size:12px;color:#444}
.bar{height:4px;background:#eee;margin-top:10px;position:relative}
.bar i{position:absolute;left:0;top:0;height:4px;width:45%;background:var(--pink)}
.playlist{margin-top:14px}
.playlist li{list-style:none;display:flex;justify-content:space-between;color:#f3c3d2;font-size:11px;padding:9px 10px;border-bottom:1px solid rgba(255,255,255,.12)}
.events li{list-style:none;display:flex;gap:12px;align-items:center;background:rgba(255,255,255,.06);margin-bottom:8px;height:54px;padding-right:10px}
.date{width:48px;height:54px;background:var(--white);color:var(--pink);text-align:center;font-family:"Titillium Web",sans-serif;font-weight:700;font-size:13px;line-height:1.1;padding-top:8px}
.date small{display:block;background:var(--pink);color:var(--white);font-size:10px;margin-top:6px;padding:2px 0}
.events .info{font-size:11px;color:#f6d3de}
.events .info b{display:block;color:var(--white);font-size:12px}

.testimonials{height:420px;background:var(--grey);padding-top:60px;text-align:center}
.testimonials h2{color:var(--ink)}
.avatars{display:flex;justify-content:center;align-items:center;gap:36px;margin-top:44px}
.avatars span{width:56px;height:56px;border-radius:50%;background:linear-gradient(#c8c8cd,#8d8d94)}
.avatars .current{width:76px;height:76px;border:3px solid var(--white);box-shadow:0 0 0 2px var(--pink)}
.reviewer{font-family:"Titillium Web",sans-serif;font-weight:700;font-size:12px;color:var(--ink);margin-top:10px;letter-spacing:1px}
.quote{width:640px;margin:18px auto 0;font-size:13px;line-height:1.7;color:#777;font-style:italic}
.dots{display:flex;justify-content:center;gap:8px;margin-top:22px}
.dots i{width:8px;height:8px;border-radius:50%;background:#ccc}
.dots i.on{background:var(--pink)}

.availability{height:760px;background:linear-gradient(135deg,var(--pink),var(--pink-dark));padding-top:60px;position:relative}
.availability h2{color:var(--white)}
.calendar{position:absolute;left:200px;top:160px;width:840px;background:var(--white);box-shadow:0 10px 30px rgba(0,0,0,.25)}
.calendar table{width:100%;border-collapse:collapse;table-layout:fixed}
.calendar th{background:var(--pink-deep);color:var(--white);font-family:"Titillium Web",sans-serif;font-weight:600;font-size:12px;height:40px}
.calendar td{height:92px;border:1px solid #eee;text-align:center;vertical-align:top;padding-top:12px;font-size:10px;color:#999}
.calendar td b{display:block;font-family:"Titillium Web",sans-serif;font-size:15px;color:var(--ink);margin-bottom:4px}
.calendar td .who{display:block;color:var(--ink);font-weight:600;font-size:11px}
.calendar td.today{box-shadow:inset 0 0 0 2px var(--pink)}

.booking{height:540px;background:var(--grey);padding-top:72px}
.booking h2{color:var(--ink)}
.form{width:800px;margin:56px auto 0;display:grid;grid-template-columns:repeat(3,1fr);gap:14px 20px}
.field{height:40px;background:var(--white);border:1px solid var(--line);font-size:10px;color:#999;letter-spacing:.5px;display:flex;align-items:center;padding:0 14px;text-transform:uppercase;justify-content:space-between}
.form .btn{height:40px;font-size:12px}

.footer{height:136px;background:var(--ink);display:flex;align-items:center;justify-content:space-between;padding:0 60px;color:#999;font-size:11px}
</style>
</head>
<body>
<div class="topbar">
  <div class="socials"><span></span><span></span><span></span><span></span><span></span></div>
  <div class="toplinks"><span>About Tolly</span><span>FAQs</span><span>Testimonials</span><span>Suppliers</span><span>Live Event Conditions</span></div>
</div>
<header class="header">
  <div class="brand"><i></i>TOLLY KESSING</div>
  <nav class="nav"><span class="active">HOME</span><span>EVENTS</span><span>MUSIC</span><span>VIDEO</span><span>REPERTOIRE</span><span>GALLERY</span><span>TESTIMONIALS</span><span class="btn">Buy CD</span></nav>
</header>

<section class="hero">
  <div class="hero-photo" role="img" aria-label="Pianist in a dark suit seated at a white grand piano"></div>
  <div class="hero-text">
    <h1>TOLLY <b>KESSING</b></h1>
    <div class="role">WEDDING PIANIST | EVENT PIANIST</div>
    <p>Tolly Kessing is Melbourne's premier award winning &amp; local pianist specialising in playing beautiful background music for weddings, special occasions &amp; corporate events.</p>
    <span class="btn">Book Now</span>
    <div class="badges"><span></span><span></span><span></span></div>
  </div>
</section>

<section class="music">
  <div class="section-title"><h2>Music &amp; Events</h2>
    <svg width="60" height="14" viewBox="0 0 60 14"><polyline points="0,7 18,7 22,2 26,12 30,2 34,12 38,7 60,7" fill="none" stroke="#fff" stroke-width="2"/></svg></div>
  <div class="music-panel">
    <div class="panel-col">
      <h3>Audio Player</h3>
      <div class="player">
        <div class="play"><svg width="18" height="18" viewBox="0 0 18 18"><polygon points="4,2 16,9 4,16" fill="#e8265a"/></svg></div>
        <div class="track">01 LANTERN HALL - MORNING LIGHT<div class="bar"><i></i></div></div>
      </div>
      <ul class="playlist">
        <li><span>01. LANTERN HALL - MORNING LIGHT</span><span>03:45</span></li>
        <li><span>02. LANTERN HALL - QUIET RIVER</span><span>04:10</span></li>
        <li><span>03. LANTERN HALL - FIRST DANCE</span><span>03:28</span></li>
        <li><span>04. LANTERN HALL - GOLDEN HOUR</span><span>04:02</span></li>
        <li><span>05. LANTERN HALL - SILVER VOWS</span><span>03:56</span></li>
        <li><span>06. LANTERN HALL - SLOW WALTZ</span><span>03:12</span></li>
        <li><span>07. LANTERN HALL - EVENING BELLS</span><span>04:21</span></li>
        <li><span>08. LANTERN HALL - HOMEWARD</span><span>03:38</span></li>
      </ul>
    </div>
    <div class="panel-col">
      <h3>Upcoming Events</h3>
      <ul class="events">
        <li><div class="date">12<small>JUL</small></div><div class="info"><b>PRIVATE EVENT - AVENDALE (TBC)</b>Jul 12 @ 7:00 pm - 10:00 pm</div></li>
        <li><div class="date">19<small>JUL</small></div><div class="info"><b>PRIVATE EVENT - AVENDALE (TBC)</b>Jul 19 @ 7:00 pm - 10:00 pm</div></li>
        <li><div class="date">26<small>JUL</small></div><div class="info"><b>PRIVATE EVENT - AVENDALE (TBC)</b>Jul 26 @ 7:00 pm - 10:00 pm</div></li>
        <li><div class="date">02<small>AUG</small></div><div class="info"><b>PRIVATE EVENT - AVENDALE (TBC)</b>Aug 2 @ 7:00 pm - 10:00 pm</div></li>
        <li><div class="date">09<small>AUG</small></div><div class="info"><b>PRIVATE EVENT - AVENDALE (TBC)</b>Aug 9 @ 7:00 pm - 10:00 pm</div></li>
        <li><div class="date">16<small>AUG</small></div><div class="info"><b>PRIVATE EVENT - AVENDALE (TBC)</b>Aug 16 @ 7:00 pm - 10:00 pm</div></li>
        <li><div class="date">23<small>AUG</small></div><div class="info"><b>PRIVATE EVENT - AVENDALE (TBC)</b>Aug 23 @ 7:00 pm - 10:00 pm</div></li>
      </ul>
    </div>
  </div>
</section>

<section class="testimonials">
  <div class="section-title"><h2>What Our Musicians Say</h2>
    <svg width="60" height="14" viewBox="0 0 60 14"><polyline points="0,7 18,7 22,2 26,12 30,2 34,12 38,7 60,7" fill="none" stroke="#e8265a" stroke-width="2"/></svg></div>
  <div class="avatars" role="img" aria-label="Musician portrait thumbnails"><span></span><span></span><span class="current"></span><span></span><span></span></div>
  <div class="reviewer">RORY VALE</div>
  <p class="quote">"It is a long established fact that a guest will be distracted by the beautiful sound of a piano when looking at the layout. The point of using a live player is that it has a more-or-less normal distribution of notes, as opposed."</p>
  <div class="dots"><i></i><i class="on"></i><i></i></div>
</section>

<section class="availability">
  <div class="section-title"><h2>Availability of Musicians</h2>
    <svg width="60" height="14" viewBox="0 0 60 14"><polyline points="0,7 18,7 22,2 26,12 30,2 34,12 38,7 60,7" fill="none" stroke="#fff" stroke-width="2"/></svg></div>
  <div class="calendar">
    <table>
      <tr><th>Monday</th><th>Tuesday</th><th>Wednesday</th><th>Thursday</th><th>Friday</th><th>Saturday</th><th>Sunday</th></tr>
      <tr><td><b>1</b></td><td><b>2</b></td><td class="today"><b>3</b><span class="who">Tolly Kessing</span>Wedding Pianist</td><td><b>4</b></td><td><b>5</b></td><td><b>6</b><span class="who">Tolly Kessing</span>Wedding Pianist</td><td><b>7</b><span class="who">Tolly Kessing</span>Wedding Pianist</td></tr>
      <tr><td><b>8</b><span class="who">Tolly Kessing</span>Wedding Pianist</td><td><b>9</b><span class="who">Tolly Kessing</span>Wedding Pianist</td><td><b>10</b><span class="who">Tolly Kessing</span>Wedding Pianist</td><td><b>11</b></td><td><b>12</b><span class="who">Tolly Kessing</span>Wedding Pianist</td><td><b>13</b><span class="who">Tolly Kessing</span>Wedding Pianist</td><td><b>14</b></td></tr>
      <tr><td><b>15</b><span class="who">Tolly Kessing</span>Wedding Pianist</td><td><b>16</b></td><td><b>17</b><span class="who">Tolly Kessing</span>Wedding Pianist</td><td><b>18</b><span class="who">Tolly Kessing</span>Wedding Pianist</td><td><b>19</b></td><td><b>20</b><span class="who">Tolly Kessing</span>Wedding Pianist</td><td><b>21</b><span class="who">Tolly Kessing</span>Wedding Pianist</td></tr>
      <tr><td><b>22</b><span class="who">Tolly Kessing</span>Wedding Pianist</td><td><b>23</b><span class="who">Tolly Kessing</span>Wedding Pianist</td><td><b>24</b></td><td><b>25</b><span class="who">Tolly Kessing</span>Wedding Pianist</td><td><b>26</b><span class="who">Tolly Kessing</span>Wedding Pianist</td><td><b>27</b></td><td><b>28</b><span class="who">Tolly Kessing</span>Wedding Pianist</td></tr>
      <tr><td><b>29</b><span class="who">Tolly Kessing</span>Wedding Pianist</td><td><b>30</b></td><td><b>31</b><span class="who">Tolly Kessing</span>Wedding Pianist</td><td><b>1</b></td><td><b>2</b><span class="who">Tolly Kessing</span>Wedding Pianist</td><td><b>3</b><span class="who">Tolly Kessing</span>Wedding Pianist</td><td><b>4</b></td></tr>
    </table>
  </div>
</section>

<section class="booking">
  <div class="section-title"><h2>Book Our Musicians</h2>
    <svg width="60" height="14" viewBox="0 0 60 14"><polyline points="0,7 18,7 22,2 26,12 30,2 34,12 38,7 60,7" fill="none" stroke="#e8265a" stroke-width="2"/></svg></div>
  <div class="form">
    <div class="field">Name</div><div class="field">Address</div><div class="field">Phone</div>
    <div class="field">Date of Function</div><div class="field">Venue Address &amp; Phone</div><div class="field">Function</div>
    <div class="field">Time</div><div class="field">Quote</div><div class="field">Other Comment <span>&#9662;</span></div>
    <div class="field">State</div><div class="field">Preferred Musician?</div><span class="btn">Book Now</span>
  </div>
</section>

<footer class="footer">
  <span>© 2017 Copyright tollykessing.com.au</span>
  <div class="socials"><span></span><span></span><span></span><span></span></div>
</footer>
</body>
</html>
```